Image-Folder for a bed house

We need an image folder for our company. This is intended both for private clients at trade fairs or for commercial customers during visits of our field staff, as a general idea of our company. We would therefore especially the "width" demonstrate our product range and customer animate in our showroom to come and take our service services. we would like to list the following topics (but can also be like a little shortened): our product ... * waterbeds * box springs * Mattresses and bed frames * Spa Beds & Property mattresses * gel beds / air beds * bedsteads / sofa * Seniors bed with lift * multifunction massage chair * Murphy bed / cot * bedding: blankets, pillows, bedding * furniture: storage systems, night tables, dressers, etc. exceptional service ... * Complete bedroom planning * Installation & bedroom wardrobes made to measure * sliding door systems to measure * Übersiedlungs- and assembly service * Annual waterbeds service The folder should of course be visually appealing and in the appendix you will find a large selection of images that you can use. Detailed information about us and our products can be found our website (www.posaru.at) and in the appendix to our previous image folder. We look forward to your suggestions !! Thanks in advance.

```html
<!DOCTYPE html>
<html lang="de">
<head>
<meta charset="utf-8">
<title>Posaru – Imagefolder</title>
<link href="https://fonts.googleapis.com/css2?family=Quicksand:wght@400;500;600&family=Mulish:wght@400;700;800&display=swap" rel="stylesheet">
<style>
:root{
  --page:#2b2b2d;
  --blue:#0b4a9e;
  --blue-mid:#1275c4;
  --blue-light:#1b8fd6;
  --yellow:#f7d42a;
  --white:#ffffff;
}
*{margin:0;padding:0;box-sizing:border-box}
html,body{width:994px;height:1200px;overflow:hidden;background:var(--page)}
.canvas{position:relative;width:994px;height:1200px}
.spread{position:absolute;left:20px;top:360px;width:954px;height:479px;background:var(--white);overflow:hidden;box-shadow:0 6px 20px rgba(0,0,0,.5);font-family:"Mulish",sans-serif}
.shape-layer{position:absolute;inset:0;width:954px;height:479px}
.photo{position:absolute}
.photo--sky{left:0;top:0;width:239px;height:200px;background:linear-gradient(180deg,#8fb6e0 0%,#c9dcef 55%,#f4f6fa 100%)}
.photo--bedroom{left:239px;top:225px;width:238px;height:185px;background:linear-gradient(160deg,#d9d6cf 0%,#8b8a86 45%,#5b4c3c 100%)}
.photo--man{left:477px;top:0;width:239px;height:230px;background:linear-gradient(180deg,#eae7e2 0%,#d2b7a3 50%,#f1efec 100%)}
.photo--woman{left:716px;top:0;width:238px;height:255px;background:linear-gradient(180deg,#eeece8 0%,#c8a38c 50%,#f4f3f0 100%)}
.panel-text{position:absolute;left:239px;top:0;width:238px;height:225px;background:linear-gradient(180deg,#fbfaf3,#f1efe4)}
.intro{position:absolute;left:272px;top:32px;width:178px;font-size:7.6px;line-height:1.38;color:var(--blue);text-align:justify}
.ref-title{position:absolute;left:272px;top:116px;font-size:10.5px;font-weight:800;color:var(--blue)}
.ref-list{position:absolute;left:272px;top:132px;list-style:none;font-size:7.6px;line-height:1.35;color:var(--blue)}
.ref-list li::before{content:"• "}
.ref-note{position:absolute;left:340px;top:211px;font-size:5.6px;color:var(--blue)}
.brand{position:absolute;display:flex;align-items:center;gap:6px;font-family:"Quicksand",sans-serif;font-weight:500}
.brand__dot{display:block;border-radius:50%}
.brand--back{left:72px;top:206px;color:var(--white);font-size:22px}
.brand--back .brand__dot{width:12px;height:12px;background:var(--white)}
.brand--front{left:770px;top:400px;color:var(--blue);font-size:28px}
.brand--front .brand__dot{width:14px;height:14px;background:var(--blue)}
.brand__sub{position:absolute;font-family:"Quicksand",sans-serif;font-size:8px;font-weight:500}
.brand__sub--back{left:84px;top:238px;color:var(--white)}
.brand__sub--front{left:784px;top:438px;color:var(--blue);font-size:9px}
.contact{position:absolute;left:0;top:266px;width:239px;text-align:center;color:var(--white);font-size:10.5px;line-height:1.35}
.contact p+p{margin-top:10px}
.web{position:absolute;left:38px;top:430px;display:flex;align-items:center;gap:10px;font-family:"Quicksand",sans-serif;font-size:17px;font-weight:500;color:var(--blue)}
.web__dot{width:12px;height:12px;border-radius:50%;background:var(--blue)}
.badge{position:absolute;display:flex;align-items:center;justify-content:center;text-align:center;border-radius:50%;font-family:"Quicksand",sans-serif;line-height:1.3}
.badge--partner{left:254px;top:358px;width:108px;height:108px;background:var(--blue-light);border:3px solid var(--blue);color:var(--white);font-size:11px}
.badge--massage{left:585px;top:246px;width:86px;height:86px;background:var(--yellow);border:3px solid var(--white);color:var(--blue);font-size:8.5px}
.wellness{position:absolute;left:512px;top:344px;width:170px;text-align:center;color:var(--white);font-size:7.4px;line-height:1.38}
.headline{position:absolute;left:730px;top:262px;width:210px;text-align:center;font-family:"Quicksand",sans-serif;font-weight:400;color:var(--blue);font-size:31px;line-height:1.04}
</style>
</head>
<body>
<main class="canvas">
  <section class="spread" aria-label="Imagefolder Innenansicht">
    <div class="photo photo--sky" role="img" aria-label="Foto: Frau schwebt schlafend auf Wolken am Himmel"></div>
    <div class="panel-text"></div>
    <div class="photo photo--bedroom" role="img" aria-label="Foto: Schlafzimmer mit Holzbett vor großem Fenster"></div>
    <div class="photo photo--man" role="img" aria-label="Foto: staunender Mann im Bett zwischen Kissen"></div>
    <div class="photo photo--woman" role="img" aria-label="Foto: begeisterte Frau im Bett mit Bettdecke"></div>

    <svg class="shape-layer" viewBox="0 0 954 479" aria-hidden="true">
      <path d="M0,182 Q120,225 239,172 L239,405 L0,392 Z" fill="var(--blue)"/>
      <path d="M0,182 Q120,225 239,172" fill="none" stroke="var(--yellow)" stroke-width="3"/>
      <rect x="716" y="255" width="238" height="110" fill="var(--white)"/>
      <path d="M0,388 C200,420 420,400 600,366 C720,346 840,336 954,342 L954,360 C840,354 720,362 600,386 C420,420 200,438 0,408 Z" fill="var(--blue)"/>
      <path d="M0,398 C200,430 420,410 600,378 C720,358 840,348 954,354 L954,368 C840,362 720,372 600,396 C420,428 200,444 0,414 Z" fill="var(--blue-mid)"/>
      <path d="M0,410 C200,442 420,426 600,392 C720,372 840,360 954,366 L954,479 L0,479 Z" fill="var(--yellow)"/>
      <path d="M492,262 C500,230 540,236 585,248 C640,262 680,240 706,262 C722,300 714,360 704,400 C690,452 640,478 596,478 C540,478 498,446 490,400 C484,350 486,300 492,262 Z" fill="var(--blue-light)" stroke="var(--white)" stroke-width="3"/>
    </svg>

    <div class="brand brand--back"><span class="brand__dot"></span>Posaru</div>
    <div class="brand__sub brand__sub--back">das Tiroler Bettenhaus</div>
    <div class="contact">
      <p>Lindenweg 24<br>A-6020 Innsbruck<br>Tel. +43(0)512/480216<br>Fax +43(0)512/480216-20<br>E-Mail: office@posaru.at</p>
      <p>Öffnungszeiten:<br>Mo-Fr 9-12, 13-18 Uhr,<br>Sa 9-12 Uhr</p>
    </div>
    <div class="web"><span class="web__dot"></span>www.posaru.at</div>

    <p class="intro">Über unsere Landesgrenzen hinaus, vertraut die Spitzenhotellerie seit vielen Jahren auf unsere Wohlfühlbetten. Zugegeben, darauf sind wir sehr stolz. Weil wir als traditionsreiches Tiroler Familienunternehmen auf diese Weise mit unseren Produkten zum Qualitätstourismus beitragen dürfen.</p>
    <h2 class="ref-title">Hier* liegt man bereits richtig:</h2>
    <ul class="ref-list">
      <li>Alpenquell Therme, Längenfeld</li>
      <li>Gourmethotel Lindenhof, Lech am Arlberg</li>
      <li>Seehotel Almrose, Achenkirch</li>
      <li>Hotel Chasa Valdora, Samnaun, CH</li>
      <li>Hotel Bergblick, Lech am Arlberg</li>
      <li>Hotel Silberhorn, Ischgl</li>
      <li>Hotel Edelweißhof, Sölden</li>
    </ul>
    <p class="ref-note">* kleiner Auszug unserer Kundenliste</p>
    <div class="badge badge--partner">First Class<br>Partner der<br>Tiroler<br>Spitzenhotellerie</div>

    <div class="badge badge--massage">Entspannen<br>Sie sich!<br>Exklusive<br>Massagesessel</div>
    <p class="wellness">Wellness für Ihr Wohnzimmer. Aktive Erholung für Ihren Körper und Geist. Hightech und Harmonie? Das schließt sich nicht aus. Im Gegenteil, wie unser großes Sortiment exklusiver Massagesessel beweist. Wir haben die Produkte der Weltmarktführer für Sie. Kurz, die besten der Besten. Multifunktional, vielseitig, zeitlos schön im Design. Und gemacht für Ihr Wohlbefinden.</p>

    <h1 class="headline">Bei uns liegen<br>Sie richtig!</h1>
    <div class="brand brand--front"><span class="brand__dot"></span>Posaru</div>
    <div class="brand__sub brand__sub--front">das Tiroler Bettenhaus</div>
  </section>
</main>
</body>
</html>
```